23rd Annual Harrowgate Lantern Film Festival Poster

Design an eye catchy, stylish poster for our 23rd film festival. Be different not just a poster with a film reel. Think outside of the box with a design that will attract peoples attention. Colorful (you choose the colors). Make it fun and creative, like the film festival. Show your talents in the design. Be sure it is new and stylish. Dates are August 21 - 29, 2020. Poster size will be 27 inches by 40 inches

Target Market(s)

Upper Middle class - movie lovers

Font styles to use
Sans Serif

Colors
33a6d7

Requirements
Must have
• NO CLIP ART - be original !
Nice to have
• abstract - think outside the box
Should not have
• CLIP ART

```html
<!DOCTYPE html>
<html lang="en">
<head>
<meta charset="utf-8">
<title>23rd Harrowgate Lantern Film Festival</title>
<link rel="stylesheet" href="https://fonts.googleapis.com/css2?family=Montserrat:wght@700;900&display=swap">
<style>
  :root {
    --paper: #ffffff;
    --ink: #111111;
    --mauve: #d6b0ae;
    --lavender: #cbbbe6;
    --sage: #cbd69c;
    --echo-pink: #ee8cc8;
    --art-yellow: #f1e04a;
    --art-grey: #d9d9d9;
    --art-blue: #33a6d7;
  }
  html, body {
    margin: 0;
    padding: 0;
    width: 810px;
    height: 1200px;
    overflow: hidden;
    background: var(--paper);
  }
  .poster {
    position: relative;
    width: 810px;
    height: 1200px;
    overflow: hidden;
    background: var(--paper);
    font-family: "Montserrat", "Arial Black", sans-serif;
  }
  .poster-art { position: absolute; inset: 0; }
  .blob-mauve { fill: var(--mauve); }
  .blob-lavender { fill: var(--lavender); }
  .blob-sage { fill: var(--sage); }
  .headline { fill: var(--ink); font-weight: 900; }
  .headline-echo { fill: var(--echo-pink); font-weight: 900; opacity: 0.6; }
  .brand-mark { fill: none; stroke: var(--ink); stroke-width: 3; }
  .brand-name { fill: var(--ink); font-weight: 700; }
  .brand-rule { stroke: var(--ink); stroke-width: 1; }
</style>
</head>
<body>
<main class="poster">
  <svg class="poster-art" width="810" height="1200" viewBox="0 0 810 1200">
    <defs>
      <linearGradient id="art-tones" x1="0" y1="0" x2="0" y2="1">
        <stop offset="0" stop-color="var(--art-yellow)"/>
        <stop offset="0.35" stop-color="var(--art-grey)"/>
        <stop offset="0.55" stop-color="var(--art-blue)"/>
        <stop offset="1" stop-color="var(--art-blue)"/>
      </linearGradient>
    </defs>

    <!-- background colour fields -->
    <path class="blob-mauve" d="M335 0 H810 V420 L760 410 L690 300 L560 250 L460 140 L330 110 Z"/>
    <path class="blob-lavender" d="M810 110 L700 130 L640 290 L660 420 L650 600 L640 760 L690 900 L640 1080 L620 1200 H810 Z"/>
    <path class="blob-sage" d="M0 440 L120 410 L260 380 L320 560 L260 720 L300 860 L270 1010 L0 1020 Z"/>

    <!-- illustration area -->
    <rect role="img" aria-label="Illustration of a seated young woman with yellow hair and a blue blouse"
          x="195" y="135" width="470" height="735" rx="40" fill="url(#art-tones)" opacity="0.9"/>

    <!-- brand -->
    <circle class="brand-mark" cx="171" cy="100" r="17"/>
    <text class="brand-name" x="171" y="143" text-anchor="middle" font-size="14" textLength="150" lengthAdjust="spacingAndGlyphs">HARROWGATE LANTERN</text>
    <line class="brand-rule" x1="95" y1="160" x2="247" y2="160"/>
    <text class="brand-name" x="171" y="173" text-anchor="middle" font-size="8" letter-spacing="0.5">FILM FESTIVAL</text>

    <!-- pink echo lettering -->
    <text class="headline-echo" x="104" y="670" font-size="124" textLength="260" lengthAdjust="spacingAndGlyphs">23<tspan font-size="64">RD</tspan></text>
    <text class="headline-echo" x="106" y="800" font-size="130" textLength="292" lengthAdjust="spacingAndGlyphs">FILM</text>
    <text class="headline-echo" x="106" y="942" font-size="130" textLength="602" lengthAdjust="spacingAndGlyphs">FESTIVAL</text>
    <text class="headline-echo" x="104" y="1025" font-size="64" textLength="598" lengthAdjust="spacingAndGlyphs">AUGUST 21-29 | 2020</text>

    <!-- main headline -->
    <text class="headline" x="98" y="663" font-size="124" textLength="260" lengthAdjust="spacingAndGlyphs">23<tspan font-size="64">RD</tspan></text>
    <text class="headline" x="98" y="810" font-size="130" textLength="292" lengthAdjust="spacingAndGlyphs">FILM</text>
    <text class="headline" x="98" y="957" font-size="130" textLength="602" lengthAdjust="spacingAndGlyphs">FESTIVAL</text>
    <text class="headline" x="96" y="1043" font-size="64" textLength="600" lengthAdjust="spacingAndGlyphs">AUGUST 21-29 | 2020</text>
  </svg>
</main>
</body>
</html>
```